Design a menu for a Pizza company

I need help designing a color menu for a pizza company. It will be a 9x16" trifold menu (3-panel). I would like to include some photos of pizza, salads, subs, sandwiches, drinks, etc. (no clipart). Attached is an example of an existing menu. I need to make the menu full color. We would like to modernize this menu with full color photos like the attached sample menu. The final files should have editable files so I can edit prices and menu items as needed. I prefer CorelDraw graphics software.

Target Market(s)

General public.

Industry/Entity Type

Restaurant

Font styles to use
Sans Serif

Colors
ec1f27
fffefc
9bcb3b

Requirements
Must have
• Must have photos and editable fonts. I will need to be able to edit the contents of the menu after you provide me with the final files.
Nice to have
• It would be nice to have this menu created in CorelDraw X7 or X8.
Should not have
• Should not have clip art or low resolution photos.

```html
<!DOCTYPE html>
<html lang="en">
<head>
<meta charset="utf-8">
<title>Pizza Menu – Inside Spread</title>
<link href="https://fonts.googleapis.com/css2?family=Arimo:wght@400;700&family=Kalam:wght@400;700&display=swap" rel="stylesheet">
<style>
  :root{
    --red:#ec1f27;
    --cream:#fffefc;
    --green:#9bcb3b;
    --ink:#2a2622;
    --ink-soft:#5b554e;
    --card:rgba(255,254,252,0.88);
    --page-bg:#e9e6e1;
    --wood-dark:#4a3a2e;
    --wood-mid:#7a5f49;
  }
  *{box-sizing:border-box;margin:0;padding:0}
  html,body{width:1200px;height:900px;overflow:hidden;background:var(--page-bg)}
  body{font-family:"Arimo",Arial,sans-serif;color:var(--ink);position:relative}

  .menu-spread{
    position:absolute;left:30px;top:130px;width:1140px;height:641px;
    display:grid;grid-template-columns:repeat(3,1fr);
    box-shadow:0 10px 30px rgba(0,0,0,.25);
  }
  .spread-photo{
    position:absolute;inset:0;
    background:
      radial-gradient(ellipse at 60% 30%, rgba(236,31,39,.55), transparent 45%),
      radial-gradient(ellipse at 20% 70%, rgba(214,170,60,.55), transparent 40%),
      radial-gradient(ellipse at 5% 20%, rgba(236,31,39,.5), transparent 25%),
      linear-gradient(120deg,var(--wood-mid),var(--wood-dark));
  }
  .panel{position:relative;padding:14px 16px;display:flex;flex-direction:column;gap:10px}
  .card{
    background:var(--card);border-radius:14px;padding:10px 16px 12px;
    font-size:10.5px;line-height:13px;
  }
  .card.grow{flex:1}
  .section + .section{margin-top:8px}
  .section-head{
    display:flex;align-items:flex-end;justify-content:space-between;
    border-bottom:1.5px solid var(--ink);padding-bottom:2px;margin-bottom:4px;
  }
  .section-title{
    font-family:"Kalam",cursive;font-weight:700;font-size:19px;line-height:22px;
    letter-spacing:1.5px;text-transform:uppercase;
  }
  .olive-sprig{width:54px;height:14px;border-radius:7px;background:var(--green);opacity:.85;margin-bottom:4px}
  .section-note{font-family:"Kalam",cursive;font-size:12px;line-height:14px;text-align:center;color:var(--ink-soft)}
  .col-heads{display:flex;justify-content:flex-end;gap:8px;font-size:9px;font-weight:700;color:var(--ink-soft)}
  .col-heads span{width:30px;text-align:right}
  .item{display:flex;align-items:baseline;gap:4px}
  .item .name{white-space:nowrap}
  .item .desc{font-size:8px;color:var(--ink-soft);white-space:nowrap;overflow:hidden;text-overflow:clip}
  .item .leader{flex:1;border-bottom:1px dotted var(--ink-soft);min-width:6px;transform:translateY(-3px)}
  .item .price{width:30px;text-align:right;font-weight:700}
  .item .price + .price{margin-left:4px}
  .pizza .item .price{width:28px}
  .footnote{font-style:italic;font-size:10px;line-height:13px;text-align:center;margin-top:auto;padding-top:10px}
  .extras{font-size:9.5px;line-height:12px;margin-top:6px}
  .extras strong{font-weight:700}
</style>
</head>
<body>
<div class="menu-spread">
  <div class="spread-photo" role="img" aria-label="Background photo of tomatoes, olive oil, bread and spices on a wooden table"></div>

  <!-- Left panel -->
  <section class="panel">
    <div class="card grow" style="display:flex;flex-direction:column">
      <div class="section">
        <div class="section-head"><h2 class="section-title">Appetizer</h2><div class="olive-sprig" role="img" aria-label="Olive branch ornament"></div></div>
        <div class="item"><span class="name">Mozzarella Sticks</span><span class="desc">served w/ Marinara sauce</span><span class="leader"></span><span class="price">6.49</span></div>
        <div class="item"><span class="name">Chicken Tenders</span><span class="desc">served w/ Honey Mustard sauce</span><span class="leader"></span><span class="price">6.49</span></div>
        <div class="item"><span class="name">Jalapeno Peppers</span><span class="desc">served w/ Marinara sauce</span><span class="leader"></span><span class="price">6.49</span></div>
        <div class="item"><span class="name">8 Piece Buffalo Wings</span><span class="desc">served w/ Blue Cheese sauce</span><span class="leader"></span><span class="price">6.99</span></div>
        <div class="item"><span class="name">Fried Mushroom</span><span class="desc">served w/ Ranch Dressing</span><span class="leader"></span><span class="price">6.49</span></div>
      </div>
      <div class="section">
        <div class="section-head"><h2 class="section-title">Side Orders</h2><div class="olive-sprig" role="img" aria-label="Olive branch ornament"></div></div>
        <div class="item"><span class="name">French Fries</span><span class="leader"></span><span class="price">2.49</span></div>
        <div class="item"><span class="name">Onion Rings</span><span class="leader"></span><span class="price">2.49</span></div>
        <div class="item"><span class="name">Garlic Bread</span><span class="leader"></span><span class="price">1.99</span></div>
        <div class="item"><span class="name">Garlic Bread w/ Cheese</span><span class="leader"></span><span class="price">2.99</span></div>
        <div class="item"><span class="name">Cole Slaw</span><span class="leader"></span><span class="price">1.99</span></div>
      </div>
      <div class="section">
        <div class="section-head"><h2 class="section-title">Garden Fresh Salads</h2><div class="olive-sprig" role="img" aria-label="Olive branch ornament"></div></div>
        <p class="section-note">Choice of Dressing:<br>Ranch, French, Italian, Blue Cheese, Thousand Island</p>
        <div class="item"><span class="name">Garden Salad</span><span class="leader"></span><span class="price">4.49</span></div>
        <div class="item"><span class="name">Chef Salad</span><span class="desc">(ham, salami, cheese &amp; hard boiled egg)</span><span class="leader"></span><span class="price">7.99</span></div>
        <div class="item"><span class="name">Greek Salad</span><span class="leader"></span><span class="price">7.99</span></div>
        <div class="item"><span class="name">Grilled Chicken Salad</span><span class="desc">(w/ cheese &amp; hard boiled egg)</span><span class="leader"></span><span class="price">7.99</span></div>
        <div class="item"><span class="name">Gyro Salad (Beef or Chicken)</span><span class="leader"></span><span class="price">7.99</span></div>
        <div class="item"><span class="name">Tuna Salad</span><span class="leader"></span><span class="price">7.99</span></div>
      </div>
      <div class="section">
        <div class="section-head"><h2 class="section-title">Sandwiches</h2><div class="olive-sprig" role="img" aria-label="Olive branch ornament"></div></div>
        <p class="section-note">All Available on Wheat, Rye, White Bread</p>
        <div class="item"><span class="name">Ham &amp; Cheese w/ LTM</span><span class="leader"></span><span class="price">5.99</span></div>
        <div class="item"><span class="name">Roast Beef w/ LTM</span><span class="leader"></span><span class="price">5.99</span></div>
        <div class="item"><span class="name">Tuna Salad w/ LTM</span><span class="leader"></span><span class="price">5.99</span></div>
        <div class="item"><span class="name">Turkey, Ham, Cheese w/ LTM</span><span class="leader"></span><span class="price">5.99</span></div>
        <div class="item"><span class="name">Turkey &amp; Cheese w/ LTM</span><span class="leader"></span><span class="price">5.99</span></div>
      </div>
      <p class="footnote">*Consuming raw or undercooked meats may increase<br>your risk of foodborne illness.*</p>
    </div>
  </section>

  <!-- Middle panel -->
  <section class="panel">
    <div class="card">
      <div class="section">
        <div class="section-head"><h2 class="section-title">Super Subs</h2><div class="olive-sprig" role="img" aria-label="Olive branch ornament"></div></div>
        <p class="section-note">Served Cold</p>
        <div class="col-heads"><span>8"</span><span>12"</span></div>
        <div class="item"><span class="name">Italian Cold Cut</span><span class="desc">(ham, salami, cheese, LT, onion, HP, OI)</span><span class="leader"></span><span class="price">6.99</span><span class="price">9.99</span></div>
        <div class="item"><span class="name">American Hero</span><span class="desc">(turkey, roast beef, cheese, LTM)</span><span class="leader"></span><span class="price">6.99</span><span class="price">9.99</span></div>
        <div class="item"><span class="name">Virginia Cold Cut</span><span class="desc">(ham, turkey, cheese, LTM)</span><span class="leader"></span><span class="price">6.99</span><span class="price">9.99</span></div>
        <div class="item"><span class="name">Tuna Salad</span><span class="desc">(w/ LTM)</span><span class="leader"></span><span class="price">6.99</span><span class="price">9.99</span></div>
        <div class="item"><span class="name">Ham &amp; Cheese</span><span class="desc">(w/ LTM)</span><span class="leader"></span><span class="price">6.99</span><span class="price">9.99</span></div>
        <div class="item"><span class="name">Turkey Sub</span><span class="desc">(w/ LTM)</span><span class="leader"></span><span class="price">6.99</span><span class="price">9.99</span></div>
        <div class="item"><span class="name">Club Sub</span><span class="desc">(turkey, ham, bacon, LTM)</span><span class="leader"></span><span class="price">6.99</span><span class="price">9.99</span></div>
        <div class="item"><span class="name">Roast Beef</span><span class="desc">(w/ LTM)</span><span class="leader"></span><span class="price">6.99</span><span class="price">9.99</span></div>
      </div>
      <div class="section">
        <div class="section-head"><h2 class="section-title">Hot Subs</h2><div class="olive-sprig" role="img" aria-label="Olive branch ornament"></div></div>
        <div class="col-heads"><span>8"</span><span>12"</span></div>
        <div class="item"><span class="name">Steak &amp; Cheese</span><span class="desc">(w/ grilled onion, LTM)</span><span class="leader"></span><span class="price">6.99</span><span class="price">9.99</span></div>
        <div class="item"><span class="name">Steak &amp; Mushroom</span><span class="desc">(w/ grilled onion, LTM)</span><span class="leader"></span><span class="price">6.99</span><span class="price">9.99</span></div>
        <div class="item"><span class="name">Steak</span><span class="desc">(w/ green peppers, grilled onion, LTM)</span><span class="leader"></span><span class="price">6.99</span><span class="price">9.99</span></div>
        <div class="item"><span class="name">Steak</span><span class="desc">(w/ onions, pizza sauce)</span><span class="leader"></span><span class="price">6.99</span><span class="price">9.99</span></div>
        <div class="item"><span class="name">Billy Dooley</span><span class="desc">(w/ steak, grilled onion, green peppers, egg)</span><span class="leader"></span><span class="price">6.99</span><span class="price">9.99</span></div>
        <div class="item"><span class="name">Tom Dooley</span><span class="desc">(w/ ham, hamburger, egg, LTM)</span><span class="leader"></span><span class="price">6.99</span><span class="price">9.99</span></div>
        <div class="item"><span class="name">Hot Sam</span><span class="desc">(w/ ham, bacon, egg, LTM)</span><span class="leader"></span><span class="price">6.99</span><span class="price">9.99</span></div>
        <div class="item"><span class="name">*Cheeseburger Sub</span><span class="desc">(w/ LTM)</span><span class="leader"></span><span class="price">6.99</span><span class="price">9.99</span></div>
        <div class="item"><span class="name">Pastrami</span><span class="desc">(w/ LTM)</span><span class="leader"></span><span class="price">6.99</span><span class="price">9.99</span></div>
        <div class="item"><span class="name">Veggie Sub</span><span class="desc">(w/ olive, green pepper, onion, mushroom, cheese, LTM)</span><span class="leader"></span><span class="price">6.99</span><span class="price">9.99</span></div>
        <div class="item"><span class="name">B.L.T.</span><span class="desc">(w/ mayonnaise)</span><span class="leader"></span><span class="price">6.99</span><span class="price">9.99</span></div>
        <div class="item"><span class="name">Crab Cake</span><span class="desc">(w/ LTM)</span><span class="leader"></span><span class="price">6.99</span><span class="price">9.99</span></div>
        <div class="item"><span class="name">Fish Filet</span><span class="desc">(w/ LTM)</span><span class="leader"></span><span class="price">6.99</span><span class="price">9.99</span></div>
        <div class="item"><span class="name">Chicken Filet</span><span class="desc">(w/ LTM)</span><span class="leader"></span><span class="price">6.99</span><span class="price">9.99</span></div>
      </div>
    </div>
    <div class="card grow">
      <div class="section">
        <div class="section-head"><h2 class="section-title">Parmigiana Subs</h2><div class="olive-sprig" role="img" aria-label="Olive branch ornament"></div></div>
        <div class="col-heads"><span>8"</span><span>12"</span></div>
        <div class="item"><span class="name">Meatball Parmigiana</span><span class="leader"></span><span class="price">6.99</span><span class="price">9.99</span></div>
        <div class="item"><span class="name">Italian Sausage Parmigiana</span><span class="leader"></span><span class="price">6.99</span><span class="price">9.99</span></div>
        <div class="item"><span class="name">Italian Sausage &amp; Green Peppers Parmigiana</span><span class="leader"></span><span class="price">6.99</span><span class="price">9.99</span></div>
        <div class="item"><span class="name">Chicken Parmigiana</span><span class="leader"></span><span class="price">6.99</span><span class="price">9.99</span></div>
        <div class="item"><span class="name">Veal Parmigiana</span><span class="leader"></span><span class="price">6.99</span><span class="price">9.99</span></div>
        <div class="item"><span class="name">Eggplant Parmigiana</span><span class="leader"></span><span class="price">6.99</span><span class="price">9.99</span></div>
      </div>
      <div class="item" style="margin-top:6px"><span class="name"><strong>GYRO</strong> Sandwich on Pita Bread (Chicken or Beef)</span><span class="leader"></span><span class="price">7.99</span></div>
      <p class="extras">Additional on subs: mushroom, green peppers ...... 1.25<br>extra meat ...... 3.99 &nbsp;&nbsp;&nbsp; cheese ...... 1.25</p>
    </div>
  </section>

  <!-- Right panel -->
  <section class="panel">
    <div class="card pizza">
      <div class="section">
        <div class="section-head"><h2 class="section-title">Pizza</h2><div class="olive-sprig" role="img" aria-label="Olive branch ornament"></div></div>
        <div class="col-heads"><span>7" Mini</span><span>10" S</span><span>12" M</span><span>14" L</span><span>16"</span></div>
        <div class="item"><span class="name">Plain Cheese</span><span class="leader"></span><span class="price">4.49</span><span class="price">6.99</span><span class="price">7.99</span><span class="price">9.49</span><span class="price">10.99</span></div>
        <div class="item"><span class="name">Pepperoni</span><span class="leader"></span><span class="price">4.99</span><span class="price">7.99</span><span class="price">8.99</span><span class="price">10.49</span><span class="price">12.99</span></div>
        <div class="item"><span class="name">Sausage</span><span class="leader"></span><span class="price">4.99</span><span class="price">7.99</span><span class="price">8.99</span><span class="price">10.49</span><span class="price">12.99</span></div>
        <div class="item"><span class="name">Hawaiian Pineapple</span><span class="leader"></span><span class="price">4.99</span><span class="price">7.99</span><span class="price">8.99</span><span class="price">10.49</span><span class="price">12.99</span></div>
        <div class="item"><span class="name">Ham</span><span class="leader"></span><span class="price">4.99</span><span class="price">7.99</span><span class="price">8.99</span><span class="price">10.49</span><span class="price">12.99</span></div>
        <div class="item"><span class="name">Ground Beef</span><span class="leader"></span><span class="price">4.99</span><span class="price">7.99</span><span class="price">8.99</span><span class="price">10.49</span><span class="price">12.99</span></div>
        <div class="item"><span class="name">Green Peppers</span><span class="leader"></span><span class="price">4.99</span><span class="price">7.99</span><span class="price">8.99</span><span class="price">10.49</span><span class="price">12.99</span></div>
        <div class="item"><span class="name">Onion</span><span class="leader"></span><span class="price">4.99</span><span class="price">7.99</span><span class="price">8.99</span><span class="price">10.49</span><span class="price">12.99</span></div>
        <div class="item"><span class="name">Black Olives</span><span class="leader"></span><span class="price">4.99</span><span class="price">7.99</span><span class="price">8.99</span><span class="price">10.49</span><span class="price">12.99</span></div>
        <div class="item"><span class="name">Mushroom</span><span class="leader"></span><span class="price">4.99</span><span class="price">7.99</span><span class="price">8.99</span><span class="price">10.49</span><span class="price">12.99</span></div>
        <div class="item"><span class="name">Bacon</span><span class="leader"></span><span class="price">4.99</span><span class="price">7.99</span><span class="price">8.99</span><span class="price">10.49</span><span class="price">12.99</span></div>
        <div class="item"><span class="name">Anchovies</span><span class="leader"></span><span class="price">4.99</span><span class="price">7.99</span><span class="price">8.99</span><span class="price">10.49</span><span class="price">12.99</span></div>
        <div class="item"><span class="name">Salami</span><span class="leader"></span><span class="price">4.99</span><span class="price">7.99</span><span class="price">8.99</span><span class="price">10.49</span><span class="price">12.99</span></div>
        <div class="item"><span class="name">Pepperoni, Mushroom, Sausage, Onion</span><span class="leader"></span><span class="price">8.25</span><span class="price">10.49</span><span class="price">13.99</span><span class="price">15.99</span><span class="price">17.99</span></div>
        <div class="item"><span class="name">Mama Mia Delight</span><span class="leader"></span><span class="price">8.25</span><span class="price">13.25</span><span class="price">16.95</span><span class="price">18.95</span><span class="price">19.99</span></div>
        <div class="item"><span class="name">White Pizza</span><span class="desc">(w/ Butter &amp; Garlic)</span><span class="leader"></span><span class="price">4.99</span><span class="price">7.99</span><span class="price">8.99</span><span class="price">10.49</span><span class="price">12.99</span></div>
        <div class="item"><span class="name">Extra Topping</span><span class="leader"></span><span class="price">.99</span><span class="price">1.89</span><span class="price">1.99</span><span class="price">1.99</span><span class="price">2.20</span></div>
      </div>
    </div>
    <div class="card grow">
      <div class="section">
        <div class="section-head"><h2 class="section-title">Sandwich Platters</h2><div class="olive-sprig" role="img" aria-label="Olive branch ornament"></div></div>
        <div class="item"><span class="name">Fresh Roast Beef on Jumbo Bun w/FF &amp; med. Drink</span><span class="leader"></span><span class="price">8.99</span></div>
        <div class="item"><span class="name">1/2 lb. Cheeseburger w/ FF &amp; med. Drink</span><span class="leader"></span><span class="price">8.99</span></div>
        <div class="item"><span class="name">BBQ Special on Jumbo Bun w/FF, cole slaw &amp; med. Drink</span><span class="leader"></span><span class="price">8.99</span></div>
        <div class="item"><span class="name">Fish Filet on Sesame Bun w/FF &amp; med. Drink</span><span class="leader"></span><span class="price">8.99</span></div>
        <div class="item"><span class="name">Crab Cake on Sesame Bun w/FF &amp; med. Drink</span><span class="leader"></span><span class="price">8.99</span></div>
        <div class="item"><span class="name">Gyro Sandwich (Beef or Chicken) w/FF &amp; med. Drink</span><span class="leader"></span><span class="price">8.99</span></div>
      </div>
      <div class="section">
        <div class="section-head"><h2 class="section-title">Sandwiches</h2><div class="olive-sprig" role="img" aria-label="Olive branch ornament"></div></div>
        <p class="section-note">Served on Sesame Bun</p>
        <div class="item"><span class="name">Roast Beef w/ LTM</span><span class="leader"></span><span class="price">4.99</span></div>
        <div class="item"><span class="name">Tuna Salad</span><span class="leader"></span><span class="price">4.99</span></div>
        <div class="item"><span class="name">Bar-B-Que w/ Cole Slaw</span><span class="leader"></span><span class="price">4.99</span></div>
        <div class="item"><span class="name">Grilled Chicken Breast</span><span class="leader"></span><span class="price">4.99</span></div>
        <div class="item"><span class="name">*Cheeseburger</span><span class="leader"></span><span class="price">3.75</span></div>
      </div>
    </div>
  </section>
</div>
</body>
</html>
```